Lift Her Forward, 2019 Save The Date

Please develop a save the date flyer our 4th Annual Lift Her Forward and See Her Rise! This event is focused on maintaining participation and appreciation for women in the design and construction industry.

This unique Forum provides a venue to engage everyone from executives to those just beginning their careers with active, hands-on sessions and vibrant networking with the best and brightest in the A/E/C industry. In our usual Q-TarVM Forum style, Keynotes become table participants and table participants become presenters, encouraging participants to assimilate what they are learning. Join local, state and national leaders and subject matter experts as we candidly explore and address the issues affecting women in our industry.

Industry/Entity Type

Construction

Font styles to use
Sans Serif

Requirements
Must have
• This is a save the date, Must have:
• Q-TarVM Logo
• Title: 4th Annual Lift Her Forward and See Her Rise!
• Date: January 25, 2019
• Location: Harbor Crest Resort and Spa, San Marcos, TX
Nice to have
• A header that can easily be pulled to add to other marketing materials and for use across other platforms (web, etc.).

```html
<!DOCTYPE html>
<html lang="en">
<head>
<meta charset="utf-8">
<title>Lift Her Forward – Save the Date 2019</title>
<link href="https://fonts.googleapis.com/css2?family=Arvo:wght@400;700&display=swap" rel="stylesheet">
<style>
  :root {
    --blue: #2b4fa6;
    --blue-deep: #233f8f;
    --green: #9bbb4c;
    --ink: #3a3a3a;
    --grey: #5a5a5a;
    --paper: #ffffff;
    --lavender: #c4c7e8;
  }
  html, body {
    margin: 0;
    padding: 0;
    overflow: hidden;
    background: var(--paper);
  }
  .flyer {
    position: relative;
    width: 867px;
    height: 1200px;
    overflow: hidden;
    font-family: "Arvo", sans-serif;
    background:
      linear-gradient(200deg, #ffffff 0%, #f4f4fb 45%, var(--lavender) 100%);
  }
  .artwork {
    position: absolute;
    inset: 0;
  }
  .headline {
    position: absolute;
    left: 0;
    right: 0;
    text-align: center;
    margin: 0;
  }
  .headline-edition {
    top: 560px;
    font-size: 90px;
    font-weight: 700;
    color: var(--blue);
    letter-spacing: -2px;
    line-height: 1;
  }
  .headline-edition sup {
    font-size: 42px;
    vertical-align: 38px;
    margin-right: 26px;
  }
  .headline-lead {
    top: 664px;
    font-size: 35px;
    font-weight: 400;
    color: var(--ink);
    word-spacing: 6px;
  }
  .headline-rise {
    top: 708px;
    font-size: 72px;
    font-weight: 700;
    color: var(--green);
    letter-spacing: -1px;
    line-height: 1;
  }
  .event-date {
    position: absolute;
    left: 173px;
    top: 812px;
    width: 523px;
    height: 67px;
    border-radius: 18px;
    background: linear-gradient(180deg, #3a5fbb 0%, var(--blue-deep) 100%);
    color: #ffffff;
    font-size: 44px;
    line-height: 67px;
    text-align: center;
    word-spacing: 8px;
  }
  .event-venue {
    position: absolute;
    left: 0;
    right: 0;
    top: 880px;
    margin: 0;
    text-align: center;
    font-size: 30px;
    line-height: 38px;
    color: var(--ink);
    font-style: normal;
  }
  .org-mark {
    position: absolute;
    left: 168px;
    top: 990px;
    width: 150px;
    height: 150px;
    border-radius: 50%;
    background: var(--blue);
  }
  .org-name {
    position: absolute;
    left: 356px;
    top: 1002px;
    margin: 0;
    font-size: 78px;
    font-weight: 400;
    color: var(--grey);
    line-height: 1;
    letter-spacing: -1px;
  }
  .org-rule {
    position: absolute;
    left: 359px;
    top: 1090px;
    width: 338px;
    height: 2px;
    background: var(--grey);
  }
  .org-full {
    position: absolute;
    left: 359px;
    top: 1100px;
    margin: 0;
    font-size: 15.5px;
    color: var(--green);
  }
</style>
</head>
<body>
<main class="flyer">
  <svg class="artwork" width="867" height="1200" viewBox="0 0 867 1200" aria-hidden="false">
    <defs>
      <clipPath id="portrait-clip">
        <path d="M0 0 H867 V520 H767 Q459 300 137 520 H0 Z"/>
      </clipPath>
      <linearGradient id="portrait-tone" x1="0" y1="0" x2="0" y2="1">
        <stop offset="0" stop-color="#4a5f9a"/>
        <stop offset="1" stop-color="#1d2e63"/>
      </linearGradient>
    </defs>

    <g class="accent-shards-left">
      <polygon points="59,83 99,234 0,218" fill="var(--blue)"/>
      <polygon points="0,205 41,245 0,285" fill="var(--blue)"/>
      <polygon points="75,309 75,393 7,360" fill="var(--blue)"/>
      <polygon points="66,347 103,337 89,387" fill="var(--green)"/>
      <polygon points="0,407 20,427 0,427" fill="var(--green)"/>
    </g>
    <g class="accent-shards-right">
      <polygon points="712,50 829,0 808,137" fill="var(--green)"/>
      <polygon points="808,30 856,16 849,63" fill="var(--blue)"/>
      <polygon points="822,117 867,90 867,163" fill="var(--green)"/>
      <polygon points="712,110 760,117 740,151" fill="var(--blue)"/>
      <polygon points="782,144 834,218 793,225" fill="var(--blue)"/>
    </g>

    <g class="portrait" clip-path="url(#portrait-clip)">
      <circle cx="459" cy="333" r="243" fill="var(--blue)"/>
      <circle cx="459" cy="333" r="230" fill="url(#portrait-tone)" role="img"
              aria-label="Portrait of a businesswoman in a dark suit, arms crossed, in front of a city skyline at dusk"/>
    </g>

    <path class="portrait-base" d="M137 520 Q459 346 767 520 Q459 578 137 520 Z" fill="var(--green)"/>
  </svg>

  <h1 class="headline headline-edition">4<sup>th</sup>Annual</h1>
  <p class="headline headline-lead">Lift Her Forward and See</p>
  <p class="headline headline-rise">Her Rise!</p>

  <div class="event-date">January 25, 2019</div>
  <address class="event-venue">Harbor Crest Resort and<br>Spa, San Marcos, TX</address>

  <div class="org-mark" aria-hidden="true"></div>
  <p class="org-name">Q-TarVM</p>
  <div class="org-rule" aria-hidden="true"></div>
  <p class="org-full">Quorum for Talent in Visionary Management</p>
</main>
</body>
</html>
```